Visitenkarten-Design für Psychiaterin
Zielgruppe
Dr. med. Monika Haberl, Ärztin, Psychotherapie für Kinder Jugendliche und Erwachsene, spezialisiert auf komplexe Posttraumatische Belastungsstörung, Dissoziative Störungen, Persönlichkeitsstörungen, Bindungsstörungen, LUMO-Mentorin
Das Design soll modern sein, Seriosität Professionalität, Dynamik und Geborgenheit ausstrahlen. Zielgruppe sind Menschen die traumatische Situationen überlebt haben.
Aufgabenstellung
Name, Fachgebiet und Spezialisierung, Telefonnummer, e-Mail
Unter Dateiupload sind Visitenkartenbeispiele die mir gefallen

```html
<!DOCTYPE html>
<html lang="de">
<head>
<meta charset="utf-8">
<title>Visitenkarte Dr. med. Monika Haberl</title>
<link rel="stylesheet" href="https://fonts.googleapis.com/css2?family=Fira+Sans+Condensed:wght@400;600&display=swap">
<style>
  :root {
    --backdrop: #bdb9b1;
    --paper: #f6f5f3;
    --ink: #555555;
    --green: #8dbe22;
    --green-text: #f4ffd2;
  }
  * { margin: 0; padding: 0; box-sizing: border-box; }
  html, body { width: 1200px; height: 807px; overflow: hidden; }
  body {
    background: var(--backdrop);
    font-family: "Fira Sans Condensed", sans-serif;
    color: var(--ink);
    position: relative;
  }
  .card {
    position: absolute;
    top: 233px;
    width: 540px;
    height: 340px;
    background: var(--paper);
    overflow: hidden;
  }
  .card--back { left: 40px; }
  .card--front { left: 620px; }

  /* back side */
  .back__intro { padding: 24px 26px 0 30px; }
  .back__name { font-weight: 600; font-size: 30px; line-height: 1.1; }
  .back__focus { font-size: 20.5px; line-height: 1.12; margin-top: 2px; }
  .back__divider {
    position: absolute; left: 0; right: 0; top: 172px;
    height: 6px; background: var(--ink);
  }
  .back__contact {
    position: absolute; left: 0; right: 0; top: 178px; bottom: 0;
    background: var(--green);
    color: var(--green-text);
    padding: 20px 30px;
    font-size: 24px; line-height: 1.25;
    font-style: normal;
  }

  /* front side */
  .front__name {
    position: absolute; right: 40px; top: 92px;
    font-weight: 600; font-size: 38px; line-height: 1;
  }
  .front__rule {
    position: absolute; left: 0; top: 140px;
    width: 505px; height: 5px; background: var(--green);
  }
  .front__role {
    position: absolute; right: 52px; top: 156px;
    text-align: right; font-size: 22px; line-height: 1.2;
  }
</style>
</head>
<body>
  <section class="card card--back">
    <div class="back__intro">
      <h1 class="back__name">Dr. med. Monika Haberl,</h1>
      <p class="back__focus">spezialisiert auf komplexe Posttraumatische Belas-<br>tungsstörung, Dissoziative Störungen, Persönlich-<br>keitsstörungen, Bindungsstörungen, LUMO-Mentorin</p>
    </div>
    <div class="back__divider"></div>
    <address class="back__contact">
      Telefon 04421-987650<br>
      Lindenweg 7 · 27649 Talbrunn<br>
      www.praxis-haberl.de · info@praxis-haberl.de
    </address>
  </section>

  <section class="card card--front">
    <h2 class="front__name">Dr. med. Monika Haberl</h2>
    <div class="front__rule"></div>
    <p class="front__role">Ärztin, Psychotherapie für Kinder,<br>Jugendliche und Erwachsene</p>
  </section>
</body>
</html>
```